Marwick Estate Services (Handyman / Home Improvement Company)

Looking for a double sided professional looking business card with Logo attached to be highlighted on one side and throwing in an image of a handyman as an option would be nice to see as well. We are a company focused on providing quality Handyman and Home improvement services in a timely manner that is done right the first time with integrity

Industry/Entity Type

Handyman / Home Improvement

Contact Information for Business Card

(LOGO, Name, Mobile and office phone numbers, email) on front side of card, (the words "The SOLUTION to all of your Handyman and Home Improvement needs" followed by "Family Owned and Operated" at the very bottom) on the back.

Colors
EB3D1F
EC4F4E
F09395
F8D3D4
FCEDEE

Requirements
Must have
• Red, Gray, Black Color scheme
Should not have
• No Yellow or Blue colors

```html
<!DOCTYPE html>
<html lang="en">
<head>
<meta charset="utf-8">
<title>Marwick Estate Services – Business Card</title>
<link href="https://fonts.googleapis.com/css2?family=Russo+One&family=Poppins:wght@400&family=Oswald:wght@500&family=EB+Garamond:ital@1&display=swap" rel="stylesheet">
<style>
  :root {
    --red: #eb3d1f;
    --red-soft: #ec4f4e;
    --ink: #111111;
    --paper: #ffffff;
    --card-dark: #1c1c1e;
    --pattern-tone: #262628;
    --rule: #9a9a9a;
    --stage: #e6e6e8;
  }
  * { box-sizing: border-box; margin: 0; padding: 0; }
  html, body { width: 1200px; height: 1108px; overflow: hidden; }
  body {
    background: var(--stage);
    position: relative;
  }
  .card {
    position: absolute;
    top: 214px;
    width: 400px;
    height: 680px;
    border-radius: 26px;
    overflow: hidden;
    box-shadow: 0 14px 30px rgba(0,0,0,.18);
  }
  .card--front { left: 140px; background: var(--paper); }
  .card--back { left: 660px; background: var(--card-dark); }

  /* front */
  .brand {
    position: absolute;
    top: 150px; left: 0; right: 0;
    display: flex; flex-direction: column; align-items: center; gap: 14px;
  }
  .brand__mark {
    width: 46px; height: 46px; background: var(--ink); border-radius: 50%;
  }
  .brand__name {
    font-family: "Russo One", sans-serif;
    color: var(--red);
    font-size: 34px;
    line-height: 1.1;
    text-align: center;
    letter-spacing: 1px;
    text-transform: uppercase;
  }
  .person {
    position: absolute;
    top: 430px; left: 0; right: 0;
    text-align: center;
    font-family: "Russo One", sans-serif;
    color: var(--red);
    font-size: 32px;
    letter-spacing: 1px;
  }
  .contact-icons {
    position: absolute;
    top: 482px; left: 40px; right: 40px;
    display: flex; align-items: center; gap: 8px;
  }
  .contact-icons__rule { flex: 1; height: 1px; background: var(--rule); }
  .contact-icons__item {
    width: 34px; height: 34px; border-radius: 6px; background: var(--red);
    display: flex; align-items: center; justify-content: center;
  }
  .contact-list {
    position: absolute;
    top: 530px; left: 0; right: 0;
    text-align: center;
    font-family: "Poppins", sans-serif;
    font-size: 24px;
    line-height: 1.3;
    color: var(--ink);
    list-style: none;
  }

  /* back */
  .pattern {
    position: absolute; inset: 0;
    background: radial-gradient(circle at 50% 40%, var(--pattern-tone), var(--card-dark) 75%);
  }
  .back-brand {
    position: absolute;
    top: 300px; right: 40px;
    display: flex; align-items: center; gap: 6px;
  }
  .back-brand__mark { width: 10px; height: 10px; background: var(--red); }
  .back-brand__name {
    font-family: "Russo One", sans-serif;
    color: var(--red);
    font-size: 13px;
    text-transform: uppercase;
  }
  .tagline {
    position: absolute;
    left: 0; right: 0; top: 470px;
    text-align: center;
    font-family: "Oswald", sans-serif;
    text-transform: uppercase;
    line-height: 1.12;
  }
  .tagline__lead { color: var(--red-soft); font-size: 30px; display: block; }
  .tagline__main { color: var(--paper); font-size: 40px; display: block; }
  .motto {
    position: absolute;
    left: 0; right: 0; bottom: 44px;
    text-align: center;
    font-family: "EB Garamond", serif;
    font-style: italic;
    color: var(--paper);
    font-size: 22px;
  }
</style>
</head>
<body>
  <section class="card card--front">
    <div class="brand">
      <span class="brand__mark"></span>
      <p class="brand__name">Marwick Estate<br>Services</p>
    </div>
    <h1 class="person">DANIEL REYES</h1>
    <div class="contact-icons">
      <span class="contact-icons__rule"></span>
      <span class="contact-icons__item" aria-label="mobile">
        <svg width="16" height="22" viewBox="0 0 16 22"><rect x="1.5" y="1.5" width="13" height="19" rx="2" fill="none" stroke="#fff" stroke-width="2"/><circle cx="8" cy="17" r="1.2" fill="#fff"/></svg>
      </span>
      <span class="contact-icons__item" aria-label="office phone">
        <svg width="22" height="20" viewBox="0 0 22 20"><path d="M2 7c0-3 4-4 9-4s9 1 9 4l-4 1-1-2H7L6 8z" fill="#fff"/><rect x="5" y="10" width="12" height="8" rx="1.5" fill="#fff"/></svg>
      </span>
      <span class="contact-icons__item" aria-label="email">
        <svg width="22" height="16" viewBox="0 0 22 16"><rect x="1" y="1" width="20" height="14" fill="none" stroke="#fff" stroke-width="2"/><path d="M1 1l10 8 10-8" fill="none" stroke="#fff" stroke-width="2"/></svg>
      </span>
      <span class="contact-icons__rule"></span>
    </div>
    <ul class="contact-list">
      <li>044-555 210 347</li>
      <li>044-555 210 348</li>
      <li>info@marwickestate.com</li>
    </ul>
  </section>

  <section class="card card--back">
    <div class="pattern" role="img" aria-label="Faint embossed repeating pattern of the company mark"></div>
    <div class="back-brand">
      <span class="back-brand__mark"></span>
      <span class="back-brand__name">Marwick Estate Services</span>
    </div>
    <p class="tagline">
      <span class="tagline__lead">Your solution to all of your</span>
      <span class="tagline__main">Handyman and home<br>improvement needs</span>
    </p>
    <p class="motto">Family Owned and Operated</p>
  </section>
</body>
</html>
```